Clipper Chatter, LLC a marketing company needs a logo and business card

I need a logo and business card design. The name of the company is Clipper Chatter, LLC. We hand marketing for vendors in barbershops. I would like for the design of the logo to communicate barbershop conversations that translate to business.

Industry/Entity Type

Marketing

Contact Information for Business Card

Logo needs to be on the business card. Need input fields for Name, Title, Phone, email

Logo Text

Clipper Chatter

Requirements
Must have
• barbershop pole of some sort
Nice to have
• Tagline: We make the talk about you

```html
<!DOCTYPE html>
<html lang="en">
<head>
<meta charset="utf-8">
<title>Clipper Chatter, LLC – Business Card</title>
<link href="https://fonts.googleapis.com/css2?family=Lato:wght@400;700;900&display=swap" rel="stylesheet">
<style>
  :root {
    --page: #e9e9ec;
    --card-red: #ec2227;
    --card-blue: #3b55a8;
    --card-white: #ffffff;
    --ink: #111111;
    --shadow: 0 14px 30px rgba(0,0,0,0.22);
  }
  * { margin: 0; padding: 0; box-sizing: border-box; }
  html, body {
    width: 1200px; height: 900px; overflow: hidden;
    background: var(--page);
    font-family: "Lato", Arial, sans-serif;
  }
  .canvas { position: relative; width: 1200px; height: 900px; }

  .card {
    position: absolute; left: 300px;
    width: 600px; height: 343px;
    box-shadow: var(--shadow);
    overflow: hidden;
  }

  /* Brand lockup */
  .brand { display: flex; align-items: center; gap: 10px; }
  .brand-mark { width: 16px; height: 16px; border-radius: 50%; flex: none; }
  .brand-name {
    font-weight: 900; font-size: 34px; letter-spacing: 0.5px;
    text-transform: uppercase; line-height: 1; white-space: nowrap;
  }

  /* Back side */
  .card-back { top: 60px; background: var(--card-red); }
  .card-back .brand {
    position: absolute; left: 0; right: 0; top: 154px;
    justify-content: center; color: var(--card-white);
  }
  .card-back .brand-mark { background: var(--card-white); }

  /* Front side */
  .card-front { top: 497px; background: var(--card-white); }
  .card-front .brand { position: absolute; left: 34px; top: 36px; color: var(--ink); }
  .card-front .brand-mark { background: var(--card-blue); }

  .contact { position: absolute; left: 34px; top: 116px; width: 300px; }
  .person-name { font-weight: 700; font-size: 22px; color: var(--ink); line-height: 1.2; }
  .person-title { font-size: 13px; color: var(--card-blue); margin-top: 2px; }

  .divider {
    position: absolute; left: 34px; right: 40px; top: 176px;
    height: 1px; background: var(--ink);
  }

  .contact-lines { position: absolute; left: 34px; top: 188px; }
  .contact-line {
    display: flex; align-items: center; gap: 8px;
    font-size: 14px; color: var(--ink); margin-bottom: 6px;
  }
  .contact-line svg { width: 13px; height: 13px; flex: none; }

  .edge-tab {
    position: absolute; right: 0; top: 150px;
    width: 14px; height: 40px; background: var(--ink);
  }

  .address {
    position: absolute; right: 40px; top: 240px;
    text-align: right; font-size: 15px; color: var(--ink); line-height: 1.35;
  }

  .bands { position: absolute; left: 0; bottom: 0; width: 600px; height: 60px; }
</style>
</head>
<body>
<main class="canvas">

  <section class="card card-back" aria-label="Card back">
    <div class="brand">
      <span class="brand-mark"></span>
      <span class="brand-name">Clipper Chatter, LLC</span>
    </div>
  </section>

  <section class="card card-front" aria-label="Card front">
    <div class="brand">
      <span class="brand-mark"></span>
      <span class="brand-name">Clipper Chatter, LLC</span>
    </div>

    <div class="contact">
      <p class="person-name">Marcus Reed</p>
      <p class="person-title">Managing Director</p>
    </div>

    <div class="divider"></div>

    <div class="contact-lines">
      <p class="contact-line">
        <svg viewBox="0 0 24 24" aria-hidden="true"><path fill="#3b55a8" d="M6.6 10.8a15.1 15.1 0 0 0 6.6 6.6l2.2-2.2c.3-.3.7-.4 1-.2 1.1.4 2.3.6 3.6.6.6 0 1 .4 1 1V20c0 .6-.4 1-1 1A17 17 0 0 1 3 4c0-.6.4-1 1-1h3.5c.6 0 1 .4 1 1 0 1.3.2 2.5.6 3.6.1.3 0 .7-.2 1z"/></svg>
        0700-555-214
      </p>
      <p class="contact-line">
        <svg viewBox="0 0 24 24" aria-hidden="true"><rect x="2" y="5" width="20" height="14" fill="#3b55a8"/><path d="M2 5l10 8 10-8" fill="none" stroke="#fff" stroke-width="1.8"/></svg>
        marcusreed@mailbox.test
      </p>
    </div>

    <span class="edge-tab"></span>

    <p class="address">Halvard House 58 Elm Street<br>Hillcrest NSW 2090</p>

    <svg class="bands" viewBox="0 0 600 60" preserveAspectRatio="none" aria-hidden="true">
      <polygon points="0,0 260,40 240,60 0,60" fill="#ec2227"/>
      <polygon points="240,60 262,34 600,34 600,60" fill="#3b55a8"/>
    </svg>
  </section>

</main>
</body>
</html>
```